Nicht nur, dass ich mit dem Design sehr zufrieden war, auch Änderungswünsche wurden zeitnah und zu meiner vollen Zufriedenheit ausgeführt.
Zielgruppe
Ich schreibe Kriminalromane
Zielgruppe sind die Leser von Kriminalromanen, Regionalkrimis
Aufgabenstellung
Hier handelt es sich um eine Kindesentführung im ländlichen Raum (Bayerischer Wald) ein Mosaik von Inzest und Tod.
Der Titel in moderner Schrift, angelehnt an die Titel der Skandinavienkrimis, sollte auch in kleiner Abbildung gut lesbar sein.
Es kommen in Kürze zwei weitere Titel, ebenfalls Kriminalromane, das Cover sollte also so gestaltet sein, dass eine durchgängige Reihe möglich ist.

```html
<!DOCTYPE html>
<html lang="de">
<head>
<meta charset="utf-8">
<title>Die Akte Wendel – Krimi</title>
<link rel="stylesheet" href="https://fonts.googleapis.com/css2?family=Satisfy&family=Rye&family=Zilla+Slab:wght@400&family=Cormorant+Garamond:wght@500&display=swap">
<style>
  :root {
    --forest-dark: #1f221f;
    --forest-mid: #4a514b;
    --forest-light: #8d948d;
    --bark: #2b2b29;
    --title-white: #f2f2f2;
    --line-grey: #b9b9b9;
    --region-grey: #8a8a8a;
    --author-grey: #8c8c8c;
    --blood: #b3000c;
  }
  * { margin: 0; padding: 0; box-sizing: border-box; }
  html, body { width: 752px; height: 1200px; overflow: hidden; background: var(--forest-dark); }
  .cover {
    position: relative;
    width: 752px;
    height: 1200px;
    overflow: hidden;
  }
  .forest-photo {
    position: absolute;
    inset: 0;
    background:
      linear-gradient(90deg, var(--bark) 0%, #3a3b38 28%, #3a3d39 33%, var(--forest-mid) 45%, #666d66 60%, var(--forest-light) 72%, #5a615a 88%, var(--forest-dark) 100%),
      var(--forest-dark);
  }
  .forest-photo::after {
    content: "";
    position: absolute;
    inset: 0;
    background: radial-gradient(ellipse at 60% 40%, rgba(255,255,255,0.08), rgba(0,0,0,0.55) 85%);
  }
  .blood-splash {
    position: absolute;
    left: 453px;
    top: 650px;
    width: 299px;
    height: 208px;
    background: radial-gradient(ellipse at 50% 45%, rgba(179,0,12,0.85) 0%, rgba(179,0,12,0.45) 40%, rgba(179,0,12,0) 72%);
  }
  .frame-lines {
    position: absolute;
    inset: 0;
    width: 752px;
    height: 1200px;
  }
  .frame-lines line, .frame-lines polyline {
    stroke: var(--line-grey);
    stroke-width: 2.5;
    fill: none;
  }
  .region {
    position: absolute;
    left: 14px;
    top: 28px;
    font-family: "Satisfy", cursive;
    font-size: 44px;
    line-height: 62px;
    color: var(--region-grey);
    opacity: 0.85;
  }
  .region span { display: block; padding-left: 54px; }
  .genre {
    position: absolute;
    left: 307px;
    top: 410px;
    font-family: "Zilla Slab", serif;
    font-size: 76px;
    letter-spacing: 10px;
    color: var(--title-white);
    line-height: 1;
  }
  .title {
    position: absolute;
    left: 28px;
    top: 640px;
    width: 470px;
    font-family: "Rye", serif;
    font-size: 80px;
    line-height: 76px;
    color: var(--title-white);
    text-align: right;
    text-shadow: 2px 3px 6px rgba(0,0,0,0.6);
  }
  .title span { display: block; }
  .title .line-one { letter-spacing: 4px; }
  .author {
    position: absolute;
    left: 400px;
    top: 930px;
    width: 300px;
    font-family: "Cormorant Garamond", serif;
    font-weight: 500;
    font-size: 28px;
    line-height: 30px;
    letter-spacing: 3px;
    color: var(--author-grey);
    text-align: center;
  }
</style>
</head>
<body>
  <main class="cover">
    <div class="forest-photo" role="img" aria-label="Dunkler Wald in Schwarz-Weiß, Hände greifen hinter Baumstämmen hervor"></div>
    <div class="blood-splash" role="img" aria-label="Roter Blutspritzer auf dem Waldboden"></div>

    <svg class="frame-lines" viewBox="0 0 752 1200" aria-hidden="true">
      <line x1="0" y1="301" x2="440" y2="113"/>
      <line x1="440" y1="113" x2="747" y2="416"/>
      <line x1="747" y1="416" x2="525" y2="629"/>
      <line x1="0" y1="341" x2="360" y2="648"/>
      <line x1="356" y1="347" x2="356" y2="539"/>
      <polyline points="752,608 621,744 752,837"/>
      <line x1="107" y1="605" x2="230" y2="722"/>
      <line x1="213" y1="612" x2="150" y2="660"/>
    </svg>

    <div class="region">Bayerischer<span>Wald</span></div>
    <div class="genre">KRIMI</div>
    <h1 class="title"><span class="line-one">DIE AKTE</span><span>WENDEL</span></h1>
    <p class="author">geschrieben von<br>tolvenkarp</p>
  </main>
</body>
</html>
```